Photography Business Card Design

I want a simple,classy design using a logo and simple font such as minion pro or similar. I have attached a logo that I quite like or am open to something similar. On the back of the card I would like the attached photo possibly with my website address on it some where. I want a matt black with silver or grey print. Possibly have the logo off to one side with the words Daniel Pettiford Photography stacked on top of each other
Updates
I am very sorry that some how I forgot to put my facebook address on the details section, www.socialpage.example/DanielPettifordPhotography
If this could be include on the card as well.
Industry/Entity Type
Business
Contact Information for Business Card
Daniel Pettiford Photography
www.danielpettifordphotography.example.au
Email: danielpettiford@wavelink.example
Phone: +61 (0)492 316 507
Logo Text
Logo styles of interest
Abstract Logo
Look and feel

```html
<!DOCTYPE html>
<html lang="en">
<head>
<meta charset="utf-8">
<title>Daniel Pettiford Photography – Business Card</title>
<link rel="stylesheet" href="https://fonts.googleapis.com/css2?family=Belleza&display=swap">
<style>
  :root {
    --card-bg: #1d1d1d;
    --accent: #1ab6e6;
    --ink: #e4e4e4;
  }
  html, body {
    margin: 0;
    padding: 0;
    width: 1200px;
    height: 741px;
    overflow: hidden;
    background: var(--card-bg);
  }
  .card {
    position: relative;
    width: 1200px;
    height: 741px;
    background: var(--card-bg);
    font-family: "Belleza", sans-serif;
  }
  .brand {
    position: absolute;
    left: 150px;
    top: 196px;
    display: flex;
    align-items: center;
    gap: 22px;
  }
  .brand-dot {
    width: 44px;
    height: 44px;
    border-radius: 50%;
    background: var(--accent);
  }
  .brand-name {
    margin: 0;
    font-size: 46px;
    font-weight: 400;
    line-height: 1;
    color: var(--accent);
    letter-spacing: 0.5px;
  }
  .owner {
    position: absolute;
    right: 137px;
    top: 390px;
    margin: 0;
    font-size: 50px;
    font-weight: 400;
    color: var(--accent);
    letter-spacing: 1px;
    line-height: 1;
  }
  .contacts {
    position: absolute;
    right: 140px;
    top: 468px;
    margin: 0;
    padding: 0;
    list-style: none;
  }
  .contact {
    display: flex;
    justify-content: flex-end;
    align-items: center;
    height: 38.5px;
    font-size: 24px;
    color: var(--ink);
  }
  .contact-icon {
    width: 32px;
    height: 32px;
    margin-left: 12px;
    flex: none;
  }
</style>
</head>
<body>
<main class="card">
  <div class="brand">
    <span class="brand-dot"></span>
    <h1 class="brand-name">Daniel Pettiford Photography</h1>
  </div>

  <h2 class="owner">Daniel Pettiford</h2>

  <ul class="contacts">
    <li class="contact">
      <span>+61 (0)492 316 507</span>
      <svg class="contact-icon" viewBox="0 0 32 32" aria-hidden="true">
        <circle cx="16" cy="16" r="14" fill="none" stroke="var(--accent)" stroke-width="2"/>
        <path d="M12 9 l3 0 l1 4 l-2 1.5 q1.5 3.5 5 5 l1.5 -2 l4 1 l0 3 q-1 1.5 -3 1.5 q-9 -1 -11 -11 q0 -2 1.5 -3z" fill="none" stroke="var(--accent)" stroke-width="1.8" stroke-linejoin="round"/>
      </svg>
    </li>
    <li class="contact">
      <span>danielpettiford@wavelink.example</span>
      <svg class="contact-icon" viewBox="0 0 32 32" aria-hidden="true">
        <circle cx="16" cy="16" r="14" fill="none" stroke="var(--accent)" stroke-width="2"/>
        <rect x="9" y="11" width="14" height="10" rx="1" fill="var(--accent)"/>
        <path d="M9.5 11.5 L16 17 L22.5 11.5" fill="none" stroke="var(--card-bg)" stroke-width="1.4"/>
      </svg>
    </li>
    <li class="contact">
      <span>www.danielpettifordphotography.example.au</span>
      <svg class="contact-icon" viewBox="0 0 32 32" aria-hidden="true">
        <circle cx="16" cy="16" r="14" fill="none" stroke="var(--accent)" stroke-width="2"/>
        <circle cx="11.5" cy="20.5" r="1.8" fill="var(--accent)"/>
        <path d="M10 15 a7 7 0 0 1 7 7" fill="none" stroke="var(--accent)" stroke-width="2"/>
        <path d="M10 10.5 a11.5 11.5 0 0 1 11.5 11.5" fill="none" stroke="var(--accent)" stroke-width="2"/>
      </svg>
    </li>
    <li class="contact">
      <span>www.socialpage.example/DanielPettifordPhotography</span>
      <svg class="contact-icon" viewBox="0 0 32 32" aria-hidden="true">
        <circle cx="16" cy="16" r="14" fill="none" stroke="var(--accent)" stroke-width="2"/>
      </svg>
    </li>
  </ul>
</main>
</body>
</html>
```